HARBEN VODKA LABELS DESIGN*

we Need a New label for Premium vodka "Harben Vodka" we are attaching design of current bottle and we need to change logo to Harben vodka with completely new design and concept . Please not that current logo is there just for example"

EXACT SIZE AND SHAPE OF LOGO ATTACHED

Logo Text

"harben vodka

```html
<!DOCTYPE html>
<html lang="sk">
<head>
<meta charset="utf-8">
<title>Harben Vodka – Label</title>
<link rel="stylesheet" href="https://fonts.googleapis.com/css2?family=Alfa+Slab+One&family=Cinzel:wght@400;700&family=Alegreya:wght@500;700&display=swap">
<style>
  :root {
    --gold-light: #f4dc8a;
    --gold: #d9a93c;
    --gold-deep: #9c6b1c;
    --wine-dark: #4a0204;
    --wine: #7a0b0e;
    --wine-bright: #a0181a;
    --silver-edge: #b3afa5;
    --silver-mid: #e4e1da;
    --silver-light: #fbfaf6;
    --cream: #f3eee6;
    --yellow: #f6d52e;
    --vodka-gold: #e0b63a;
    --brand-red: #5b080a;
    --quality-red: #9b1a10;
    --star-dark: #2e2b2b;
  }
  * { margin: 0; padding: 0; box-sizing: border-box; }
  html, body { width: 1200px; height: 2585px; overflow: hidden; background: #ffffff; }
  .canvas { position: relative; width: 1200px; height: 2585px; overflow: hidden; }
  .stage {
    position: absolute; left: 0; top: 0;
    width: 686px; height: 1474px;
    transform: scale(1.7493, 1.7537); transform-origin: 0 0;
  }
  .label-shape { position: absolute; inset: 0; width: 686px; height: 1474px; }
  .text { position: absolute; left: 0; width: 686px; text-align: center; white-space: nowrap; }

  .anno, .year {
    position: absolute; top: 303px; font-family: "Cinzel", serif; font-size: 20px;
    letter-spacing: 4px; color: var(--yellow);
  }
  .anno { left: 50px; }
  .year { right: 44px; }

  .brand-name {
    top: 358px; font-family: "Alfa Slab One", serif; font-size: 112px; line-height: 1;
    letter-spacing: 1px; color: var(--brand-red);
    -webkit-text-stroke: 2px var(--gold);
    transform: scaleX(0.86);
  }
  .subtitle {
    top: 563px; font-family: "Cinzel", serif; font-weight: 700; font-size: 36px; letter-spacing: 7px;
    color: var(--cream);
  }
  .product {
    top: 700px; font-family: "Alfa Slab One", serif; font-size: 126px; line-height: 1;
    letter-spacing: 6px; color: var(--vodka-gold);
    -webkit-text-stroke: 3px #5a0a08;
    transform: scaleX(0.84);
  }
  .filtered {
    top: 916px; font-family: "Cinzel", serif; font-size: 31px; letter-spacing: 3px;
    color: var(--yellow);
  }
  .story {
    top: 1018px; font-family: "Alegreya", serif; font-weight: 500; font-size: 26px;
    line-height: 38px; color: var(--yellow);
  }
  .story-last {
    top: 1100px; font-family: "Alegreya", serif; font-weight: 500; font-size: 26px;
    color: var(--wine);
  }
  .quality {
    top: 1203px; font-family: "Cinzel", serif; font-weight: 700; font-size: 29px;
    letter-spacing: 4px; color: var(--quality-red);
  }
  .volume, .strength {
    position: absolute; top: 1290px; font-family: "Alegreya", serif; font-weight: 700;
    font-size: 17px; color: var(--wine);
  }
  .volume { left: 75px; }
  .strength { right: 72px; }

  .distillery-name {
    top: 200px; font-family: "Cinzel", serif; font-weight: 700; font-size: 22px;
    letter-spacing: 2px; color: var(--wine);
  }
</style>
</head>
<body>
<main class="canvas">
  <div class="stage">
    <svg class="label-shape" viewBox="0 0 686 1474" aria-hidden="true">
      <defs>
        <path id="label-outline" d="M0,250 Q0,185 62,172 C150,45 250,6 343,6 C436,6 536,45 624,172 Q686,185 686,250 L686,1262 Q686,1334 624,1346 C536,1442 436,1468 343,1468 C250,1468 150,1442 62,1346 Q0,1334 0,1262 Z"/>
        <linearGradient id="gold-frame" x1="0" y1="0" x2="1" y2="1">
          <stop offset="0" stop-color="var(--gold-light)"/>
          <stop offset="0.4" stop-color="var(--gold)"/>
          <stop offset="0.7" stop-color="var(--gold-deep)"/>
          <stop offset="1" stop-color="var(--gold-light)"/>
        </linearGradient>
        <linearGradient id="wine-body" x1="0" y1="0" x2="1" y2="0">
          <stop offset="0" stop-color="var(--wine)"/>
          <stop offset="0.15" stop-color="var(--wine-bright)"/>
          <stop offset="0.55" stop-color="var(--wine-dark)"/>
          <stop offset="0.88" stop-color="var(--wine-bright)"/>
          <stop offset="1" stop-color="var(--wine)"/>
        </linearGradient>
        <linearGradient id="silver-band" x1="0" y1="0" x2="1" y2="0">
          <stop offset="0" stop-color="var(--silver-edge)"/>
          <stop offset="0.25" stop-color="var(--silver-mid)"/>
          <stop offset="0.5" stop-color="var(--silver-light)"/>
          <stop offset="0.75" stop-color="var(--silver-mid)"/>
          <stop offset="1" stop-color="var(--silver-edge)"/>
        </linearGradient>
        <clipPath id="inner-area">
          <use href="#label-outline" transform="translate(343 737) scale(0.925 0.964) translate(-343 -737)"/>
        </clipPath>
        <polygon id="star" points="0,-14 4,-4.5 14,-4.3 6.3,2 9,12 0,6.3 -9,12 -6.3,2 -14,-4.3 -4,-4.5"/>
      </defs>

      <use class="frame-outer" href="#label-outline" fill="url(#gold-frame)"/>
      <use class="frame-rim" href="#label-outline" fill="var(--wine)" transform="translate(343 737) scale(0.985 0.993) translate(-343 -737)"/>
      <use class="frame-line" href="#label-outline" fill="url(#gold-frame)" transform="translate(343 737) scale(0.945 0.975) translate(-343 -737)"/>

      <g clip-path="url(#inner-area)">
        <rect class="body-wine" x="0" y="0" width="686" height="1474" fill="url(#wine-body)"/>
        <rect class="band-brand" x="0" y="330" width="686" height="197" fill="url(#silver-band)"/>
        <rect class="band-footer" x="0" y="1097" width="686" height="400" fill="url(#silver-band)"/>
      </g>

      <g class="stars-top" fill="var(--gold)">
        <use href="#star" x="236" y="90"/>
        <use href="#star" x="287" y="68"/>
        <use href="#star" x="343" y="60"/>
        <use href="#star" x="399" y="68"/>
        <use href="#star" x="452" y="90"/>
      </g>

      <circle class="distillery-seal" cx="343" cy="215" r="84" fill="var(--cream)" stroke="var(--gold)" stroke-width="6"/>

      <g class="stars-bottom" fill="var(--star-dark)">
        <use href="#star" x="234" y="1357"/>
        <use href="#star" x="287" y="1378"/>
        <use href="#star" x="343" y="1385"/>
        <use href="#star" x="399" y="1378"/>
        <use href="#star" x="452" y="1357"/>
      </g>
    </svg>

    <div class="text distillery-name">TATRIN</div>

    <span class="anno">ANNO</span>
    <span class="year">1867</span>

    <h1 class="text brand-name">HARBEN</h1>
    <p class="text subtitle">EXTRA LEMNA</p>
    <h2 class="text product">VODKA</h2>
    <p class="text filtered">STRIEBROM FILTROVANA</p>
    <p class="text story">Filtracia cez 24 specialnych filtrov z aktivneha<br>striebra a kristalove cista tatranska voda, dava</p>
    <p class="text story-last">nasy vodke Extra jemnii chut a vonu</p>
    <p class="text quality">EXTRA FINE QUALITY</p>
    <span class="volume">1000 ML</span>
    <span class="strength">38% OBJ</span>
  </div>
</main>
</body>
</html>
```